Tidewren steakhouse dl flyer

We need a simple dl flyer for our restaurant tidewren steakhouse. (formerly plums restaurant at tidewren lodge, drifting gull mountain, BC Canada)
DL format. double sided. Front Could be the same as poster, back to have additional photos and info.

Perhaps a stock photo of a Plated steak, and people at a bar is also needed.

Target Market(s)

25 to 55 year old skiers, couples, families

Industry/Entity Type

Restaurant

Requirements
Must have
• must tie in with the Tidewren steakhouse poster.
Nice to have
• warm tones that tie in with the black poster, and flame grilled steak.
Should not have
• bright colours

```html
<!DOCTYPE html>
<html lang="en">
<head>
<meta charset="utf-8">
<title>Tidewren Steakhouse – DL Flyer</title>
<link rel="stylesheet" href="https://fonts.googleapis.com/css2?family=Oswald:wght@300;400&family=Roboto+Slab:wght@400;900&family=Lato:wght@400&display=swap">
<style>
  :root{
    --canvas:#e9e9e9;
    --paper:#ffffff;
    --charcoal:#323232;
    --slate:#5f5f5f;
    --ash:#8a8a8a;
    --ink:#454545;
    --white:#ffffff;
    --photo-warm-a:#8a5a3c;
    --photo-warm-b:#e8e2da;
    --photo-food-a:#f2efea;
    --photo-food-b:#6b4a36;
    --photo-bar-a:#a84a32;
    --photo-bar-b:#3a2a22;
    --photo-wine-a:#b25a44;
    --photo-wine-b:#2d3a2a;
  }
  *{margin:0;padding:0;box-sizing:border-box}
  html,body{width:1200px;height:1200px;overflow:hidden;background:var(--canvas)}
  .canvas{position:relative;width:1200px;height:1200px}
  .flyer{position:absolute;top:90px;width:601px;height:1275px;transform:scale(.8);transform-origin:0 0;background:var(--paper);overflow:hidden;box-shadow:0 6px 18px rgba(0,0,0,.18)}
  .flyer--front{left:76px}
  .flyer--back{left:643px}
  .flyer svg.shapes{position:absolute;inset:0;width:601px;height:1275px}

  .brand{position:absolute;top:34px;left:0;width:601px;text-align:center;color:var(--white);font-family:'Oswald',sans-serif;font-weight:300;font-size:36px;line-height:38px;letter-spacing:3px}
  .brand__mark{display:block;width:40px;height:40px;border:2px solid var(--white);border-radius:50%;margin:0 auto 12px}
  .brand__rule{display:block;width:258px;height:1px;background:var(--white);margin:0 auto 6px}

  .title{position:absolute;left:0;width:601px;text-align:center;font-family:'Roboto Slab',serif}
  .title__lead{top:760px;font-weight:400;font-size:36px;color:var(--slate);letter-spacing:1px}
  .title__main{top:800px;font-weight:900;font-size:72px;color:var(--charcoal);letter-spacing:1px}

  .front-footer{position:absolute;top:1224px;left:0;width:601px;text-align:center;color:var(--white);font-size:21px;white-space:nowrap}
  .front-footer__phone{font-family:'Roboto Slab',serif;font-weight:900}
  .front-footer__sep{display:inline-block;width:1px;height:22px;background:var(--white);margin:0 12px;vertical-align:-3px}
  .front-footer__web{font-family:'Roboto Slab',serif;font-weight:400;letter-spacing:3px}

  .intro{position:absolute;top:58px;left:45px;width:518px;font-family:'Oswald',sans-serif;font-weight:300;font-size:19px;line-height:23px;color:var(--ink);text-align:justify}
  .intro p{margin-bottom:23px}

  .hours{position:absolute;left:266px;top:274px;width:304px;height:304px;border-radius:50%;text-align:center;color:var(--white)}
  .hours__head{margin-top:44px;font-family:'Roboto Slab',serif;font-weight:900;font-size:17px;letter-spacing:.5px}
  .hours__rule{width:160px;height:2px;background:var(--white);margin:14px auto 8px}
  .hours__item{font-family:'Oswald',sans-serif;font-weight:300;font-size:28px;line-height:32px}
  .hours__note{font-family:'Lato',sans-serif;font-size:11px;line-height:13px;margin-top:6px}

  .reserve{position:absolute;left:42px;top:1114px;width:270px;color:var(--white);font-family:'Roboto Slab',serif;font-weight:400;font-size:16px;line-height:21px;white-space:nowrap}
  .reserve__phone{font-weight:900;font-size:33px;line-height:40px;margin:4px 0 2px}
  .reserve__time{font-weight:900;font-size:21px;line-height:26px}
</style>
</head>
<body>
<div class="canvas">

  <!-- FRONT -->
  <section class="flyer flyer--front">
    <svg class="shapes" viewBox="0 0 601 1275">
      <defs>
        <radialGradient id="dining" cx="50%" cy="45%" r="60%">
          <stop offset="0" stop-color="var(--photo-warm-b)"/>
          <stop offset="1" stop-color="var(--photo-warm-a)"/>
        </radialGradient>
        <radialGradient id="plateA" cx="50%" cy="50%" r="60%">
          <stop offset="0" stop-color="var(--photo-food-b)"/>
          <stop offset="1" stop-color="var(--photo-food-a)"/>
        </radialGradient>
        <radialGradient id="plateB" cx="50%" cy="45%" r="60%">
          <stop offset="0" stop-color="var(--photo-food-b)"/>
          <stop offset=".55" stop-color="var(--photo-food-a)"/>
          <stop offset="1" stop-color="#3c3c3c"/>
        </radialGradient>
      </defs>
      <path d="M0 0H601V420C560 620 420 720 240 712C130 708 50 680 0 650Z" fill="var(--charcoal)"/>
      <path d="M445 0H601V520C595 300 540 120 445 0Z" fill="var(--slate)"/>
      <circle cx="301" cy="452" r="264" fill="var(--white)"/>
      <circle cx="301" cy="452" r="258" fill="var(--slate)"/>
      <circle cx="301" cy="452" r="250" fill="url(#dining)" role="img" aria-label="Photo: wine glasses and flowers on a set dining table"/>
      <circle cx="301" cy="452" r="170" fill="none" stroke="var(--white)" stroke-opacity=".45" stroke-width="8"/>

      <path d="M0 1275V1205C110 1110 450 1080 601 1160V1275Z" fill="var(--white)"/>
      <path d="M0 1275V1215C120 1130 450 1110 601 1185V1275Z" fill="var(--slate)"/>
      <path d="M0 1275V1230C140 1150 450 1135 601 1205V1275Z" fill="var(--charcoal)"/>

      <circle cx="185" cy="1085" r="110" fill="var(--slate)"/>
      <circle cx="185" cy="1085" r="103" fill="var(--white)"/>
      <circle cx="185" cy="1085" r="98" fill="url(#plateA)" role="img" aria-label="Photo: plated meat with roasted peppers and herbs"/>
      <circle cx="415" cy="1042" r="132" fill="var(--slate)"/>
      <circle cx="415" cy="1042" r="125" fill="var(--white)"/>
      <circle cx="415" cy="1042" r="119" fill="url(#plateB)" role="img" aria-label="Photo: stacked steak on purple mash with red pepper"/>
    </svg>

    <div class="brand">
      <span class="brand__mark"></span>
      <span class="brand__rule"></span>
      TIDEWREN<br>STEAKHOUSE
    </div>

    <div class="title title__lead">THE TIDEWREN</div>
    <div class="title title__main">STEAKHOUSE</div>

    <div class="front-footer">
      <span class="front-footer__phone">250-555-0148</span><span class="front-footer__sep"></span><span class="front-footer__web">www.tidewrensteak.com</span>
    </div>
  </section>

  <!-- BACK -->
  <section class="flyer flyer--back">
    <svg class="shapes" viewBox="0 0 601 1275">
      <defs>
        <radialGradient id="steak" cx="62%" cy="50%" r="65%">
          <stop offset="0" stop-color="var(--photo-food-b)"/>
          <stop offset=".5" stop-color="var(--photo-food-a)"/>
          <stop offset="1" stop-color="#7a7a72"/>
        </radialGradient>
        <linearGradient id="bar" x1="0" y1="0" x2="0" y2="1">
          <stop offset="0" stop-color="var(--photo-bar-a)"/>
          <stop offset="1" stop-color="var(--photo-bar-b)"/>
        </linearGradient>
        <linearGradient id="wine" x1="0" y1="0" x2="1" y2="1">
          <stop offset="0" stop-color="var(--photo-wine-a)"/>
          <stop offset=".6" stop-color="var(--photo-wine-b)"/>
          <stop offset="1" stop-color="#c9a57e"/>
        </linearGradient>
      </defs>
      <path d="M0 0H430L420 20H0Z" fill="var(--charcoal)"/>
      <path d="M445 0H601V20H436Z" fill="var(--slate)"/>

      <path d="M0 500C90 440 200 410 300 405V440C190 450 90 480 0 530Z" fill="var(--slate)"/>
      <path d="M0 540C90 490 200 460 310 455H601V1275H0Z" fill="url(#steak)" role="img" aria-label="Photo: plated steak stack with sauce, microgreens and red pepper"/>
      <path d="M0 545C90 495 200 465 310 460" fill="none" stroke="var(--white)" stroke-width="8"/>

      <path d="M540 560C570 580 590 600 601 620V590C585 575 565 560 545 550Z" fill="var(--white)"/>

      <path d="M320 1275C300 1100 360 950 470 915C520 900 570 905 601 915V1275Z" fill="var(--white)"/>
      <path d="M332 1275C312 1110 370 960 475 927C525 913 570 917 601 925V1275Z" fill="url(#wine)" role="img" aria-label="Photo: wine bottles resting in a wooden rack"/>

      <path d="M0 1275V1075C70 1010 120 995 200 985L300 1275Z" fill="var(--white)"/>
      <path d="M0 1275V1090C70 1030 130 1010 210 1000L310 1275Z" fill="var(--slate)"/>
      <path d="M0 1275V1105C80 1045 140 1030 220 1020L318 1275Z" fill="var(--charcoal)"/>

      <circle cx="281" cy="975" r="130" fill="var(--slate)"/>
      <circle cx="281" cy="975" r="123" fill="var(--white)"/>
      <circle cx="281" cy="975" r="117" fill="url(#bar)" role="img" aria-label="Photo: guests seated at a warmly lit bar"/>

      <circle cx="418" cy="427" r="162" fill="var(--slate)"/>
      <circle cx="418" cy="427" r="153" fill="var(--white)"/>
      <circle cx="418" cy="427" r="148" fill="var(--slate)"/>
    </svg>

    <div class="intro">
      <p>The Tidewren Steakhouse provides a casual, yet unparalleled mountain dining experience that is inspired by locally sourced food and wines from British Columbia.</p>
      <p>Here you can sample the best of Rocky Mountain Cuisine such as Elk, Bison, Beef and Salmon.</p>
      <p>We are conveniently located at Tidewren Lodge, Drifting Gull Mountain Resort.</p>
    </div>

    <div class="hours">
      <div class="hours__head">OPENING HOURS</div>
      <div class="hours__rule"></div>
      <div class="hours__item">Dinner<br>5pm to 10pm</div>
      <div class="hours__rule"></div>
      <div class="hours__item">Breakfast<br>7am to 10am</div>
      <div class="hours__rule" style="margin-bottom:0"></div>
      <div class="hours__note">(Bookings essential for<br>non-house guests)</div>
    </div>

    <div class="reserve">
      For reservations call
      <div class="reserve__phone">250-555-0148</div>
      and leave a message Confirmation<br>
      of reservation call backs will be<br>
      done between <span class="reserve__time">4pm - 5pm</span>
    </div>
  </section>

</div>
</body>
</html>
```